Workout book cover design: Looking for Simple Classic Cover

I need a book cover design for "The Steady Middle". A book on exercises to strengthen the pelvic floor. Basically it's exercises for your torso and hips. I want something tasteful and classic looking.

I like this book cover design: http://www.pagelorn-books.example/Calm-Starters-Gentle-Routines-Ease-ebook/dp/Q93KX7TM41/ref=sr_1_40?ie=UTF8&qid=2958173306&sr=8-40&keywords=exercise+books

Book Title: The Steady Middle
Description to go under title: I'm working on that now and will have ready by the end of the project. (The hidden world of pelvic floor training. Discover the best exercises for creating a strong core, hips and pelvis today!)

Target Market(s)

Mostly women 35-65 and men 60+

Industry/Entity Type

Health And Wellness

Requirements
Must have
• ebook dementions: 1536 x 2048 I think works for all the online publishing companies
• 8x10 for print
Nice to have
• I like this book cover design: http://www.pagelorn-books.example/Calm-Starters-Gentle-Routines-Ease-ebook/dp/Q93KX7TM41/ref=sr_1_40?ie=UTF8&qid=2958173306&sr=8-40&keywords=exercise+books
• This cover is also ok, but no shiny. http://www.pagelorn-books.example/Bedrock-Renew-The-Climb-Poise/dp/4827305519/ref=sr_1_2?ie=UTF8&qid=2958176642&sr=8-2&keywords=foundation+book
Should not have
• I do not like this cover, it's crowded. http://www.pagelorn-books.example/Gym-Drills-Selfweight-flexing-drills-ebook/dp/Q71RWJZNHE/ref=sr_1_2?ie=UTF8&qid=2958174418&sr=8-2&keywords=workout+books
• I do not want anyone on the cover making eye contact.

```html
<!DOCTYPE html>
<html lang="en">
<head>
<meta charset="utf-8">
<title>The Steady Middle — Book Cover</title>
<link rel="stylesheet" href="https://fonts.googleapis.com/css2?family=Arimo:ital,wght@0,400;1,400&display=swap">
<style>
  :root {
    --cover-blue: #2b7cbd;
    --type-light: #a9d5f3;
    --ring-light: #a6d2f1;
    --xray-dark: #02050a;
    --xray-deep: #0b2a4d;
    --xray-mid: #2a6eb0;
    --xray-glow: #6fb4ec;
  }
  html, body {
    margin: 0;
    padding: 0;
    overflow: hidden;
    background: var(--cover-blue);
  }
  .cover {
    position: relative;
    width: 960px;
    height: 1200px;
    background: var(--cover-blue);
    font-family: "Arimo", Arial, sans-serif;
    color: var(--type-light);
    overflow: hidden;
  }
  .cover-title {
    margin: 0;
    font-weight: 400;
  }
  .title-lead {
    position: absolute;
    top: 36px;
    left: 0;
    width: 100%;
    text-align: center;
    font-style: italic;
    font-size: 67px;
    line-height: 1;
  }
  .title-main {
    position: absolute;
    top: 108px;
    left: 0;
    width: 100%;
    text-align: center;
    font-size: 136px;
    line-height: 1;
    letter-spacing: 1px;
  }
  .anatomy-frame {
    position: absolute;
    left: 180px;
    top: 290px;
    width: 600px;
    height: 600px;
  }
  .anatomy-ring { fill: var(--ring-light); }
  .anatomy-base { fill: var(--xray-dark); }
  .stop-glow { stop-color: var(--xray-glow); }
  .stop-mid { stop-color: var(--xray-mid); }
  .stop-deep { stop-color: var(--xray-deep); }
  .stop-dark { stop-color: var(--xray-dark); }
  .tagline {
    position: absolute;
    top: 924px;
    left: 0;
    width: 100%;
    margin: 0;
    text-align: center;
    font-size: 26.5px;
    line-height: 1.2;
    white-space: nowrap;
  }
  .author {
    position: absolute;
    top: 1086px;
    left: 0;
    width: 100%;
    margin: 0;
    text-align: center;
    font-size: 62px;
    line-height: 1;
  }
</style>
</head>
<body>
  <main class="cover">
    <h1 class="cover-title">
      <span class="title-lead">The Steady</span>
      <span class="title-main">MIDDLE</span>
    </h1>

    <svg class="anatomy-frame" viewBox="0 0 600 600" width="600" height="600">
      <defs>
        <radialGradient id="xrayTone" cx="50%" cy="40%" r="58%" fx="50%" fy="36%">
          <stop offset="0%" class="stop-glow" stop-opacity="0.95"/>
          <stop offset="30%" class="stop-mid" stop-opacity="0.9"/>
          <stop offset="62%" class="stop-deep"/>
          <stop offset="100%" class="stop-dark"/>
        </radialGradient>
      </defs>
      <circle class="anatomy-ring" cx="300" cy="300" r="296"/>
      <circle class="anatomy-base" cx="300" cy="300" r="290"/>
      <circle cx="300" cy="300" r="290" fill="url(#xrayTone)"
              role="img" aria-label="Glowing blue x-ray style illustration of the lower spine, pelvis and hip joints on black"/>
    </svg>

    <p class="tagline">Discover the best exercises for creating a strong core, hips and pelvis today!</p>

    <p class="author">Clara Wendt</p>
  </main>
</body>
</html>
```